Autism Center Needs a Brochure Design

We are looking for a new and improved brochure design for our Autism Center serving Northern Indiana. We provide ABA therapy for children who are on the autism spectrum. We would like to see designs that reflect some of our other marketing material and use our companies colors (blue, yellow and green). For more specific colors, look at our company logo I have uploaded below. I have also uploaded a outline of all of the information we want in the brochure and what content we want on each page.
- Calibri, Times

```html
<!DOCTYPE html>
<html lang="en">
<head>
<meta charset="utf-8">
<title>Harborview Autism Center – Brochure Option 1</title>
<link rel="stylesheet" href="https://fonts.googleapis.com/css2?family=Arimo:wght@400;700&family=Tinos:ital,wght@0,400;0,700;1,400&display=swap">
<style>
  :root{
    --page-bg:#e6e6e6;
    --navy:#2a5ea8;
    --sky:#1b8fd8;
    --pale:#d5eaf8;
    --sun:#f5c400;
    --leaf:#4caf5a;
    --ink:#3a3a3a;
    --label:#8a8a8a;
    --option:#1f9a3c;
    --white:#ffffff;
  }
  *{box-sizing:border-box;margin:0;padding:0}
  html,body{width:809px;height:1200px;overflow:hidden;background:var(--page-bg)}
  body{position:relative;font-family:"Tinos","Times New Roman",serif;color:var(--ink)}
  .option-title{position:absolute;top:4px;left:0;width:809px;text-align:center;font-family:"Arimo",Arial,sans-serif;font-weight:700;font-size:27px;color:var(--option)}
  .panel{position:absolute;overflow:hidden;border:1px solid #9aa9b8}
  .photo{position:absolute;left:0;width:100%}
  .strip{position:absolute;left:0;width:100%;height:23px;display:flex}
  .strip span{height:100%}
  .strip .b{background:var(--sky)}
  .strip .n{background:var(--navy)}
  .strip .y{background:var(--sun)}
  .strip .g{background:var(--leaf);flex:1}
  .body{position:absolute;left:0;width:100%}
  .navy{background:var(--navy);color:var(--white)}
  .pale{background:var(--pale)}
  .page-label{position:absolute;width:254px;text-align:center;font-family:"Arimo",Arial,sans-serif;font-size:15px;color:var(--label)}
  h2{font-weight:700;font-size:13px;line-height:1.25}
  p,li{font-size:9px;line-height:1.6}
  .wordmark{display:flex;align-items:center;justify-content:center;gap:6px;font-family:"Tinos","Times New Roman",serif;font-weight:700;font-size:21px;color:var(--navy)}
  .wordmark .dot{width:12px;height:12px;border-radius:50%;background:var(--sun)}
  .diff{padding:45px 26px 0}
  .diff ul{list-style:none;margin-top:12px}
  .diff li{font-size:9px;line-height:1.65}
  .contact{text-align:center;font-size:9px;line-height:1.6;padding-top:22px}
  .contact b{display:block}
  .contact .web{font-weight:700;font-size:11px;margin-top:10px;line-height:1.45}
  .contact .call{font-weight:700;font-size:14px;margin-top:6px}
  .cover{text-align:center}
  .tagline{font-size:21px;line-height:1.2;text-align:left;padding-left:32px;margin-top:20px;color:var(--ink)}
  .tagline .c1{color:var(--leaf)}
  .tagline .c2{color:var(--sun)}
  .cover h3{font-size:12px;font-weight:700;margin-top:18px}
  .cover .mini{font-size:8px;font-weight:700;line-height:1.6;margin-top:12px}
  .copy{padding:18px 24px 0 26px}
  .copy p{text-align:justify;margin-top:10px}
  .copy p.lead{margin-top:8px}
  .copy ul{list-style:none;margin-top:6px}
  .copy li{font-size:8.6px;line-height:1.5}
</style>
</head>
<body>
  <div class="option-title">option 1</div>

  <!-- Outside: Page 5 -->
  <section class="panel" style="left:24px;top:50px;width:254px;height:529px">
    <div class="photo" role="img" aria-label="Photo of a therapist working one-on-one with a boy at a table" style="top:0;height:230px;background:linear-gradient(135deg,#cfd6dc,#7e8b98 60%,#3b4a5c)"></div>
    <div class="strip" style="top:230px"><span class="b" style="width:149px"></span><span class="y" style="width:25px"></span><span class="g"></span></div>
    <div class="body navy diff" style="top:253px;height:276px">
      <h2>The Harborview Difference.</h2>
      <ul>
        <li>• Community based and family focused</li>
        <li>• Intensive, daily center based ABA therapy</li>
        <li>• We do all insurance billing and processing</li>
        <li>• No upfront costs</li>
        <li>• Full time onsite BCBA supervision</li>
        <li>• Open year round</li>
      </ul>
    </div>
  </section>

  <!-- Outside: Back page 6 -->
  <section class="panel" style="left:278px;top:50px;width:253px;height:529px">
    <div class="photo" role="img" aria-label="Photo of the brick center building entrance with a walkway and lawn" style="top:0;height:230px;background:linear-gradient(180deg,#8fc0e6 0%,#8a5a44 40%,#6f4a3a 70%,#5f9a48 100%)"></div>
    <div class="strip" style="top:230px"><span class="b" style="width:149px"></span><span class="y" style="width:25px"></span><span class="g"></span></div>
    <div class="body pale" style="top:253px;height:82px;display:flex;align-items:center;justify-content:center">
      <div class="wordmark"><span class="dot"></span>Harborview</div>
    </div>
    <div class="body navy contact" style="top:335px;height:194px">
      <b>Willow Bend Parkway</b>
      2810 Willow Bend Parkway, Brookfield, IN 46500
      <b>Cedar Commons</b>
      418 Cedar Commons Lane, Brookfield, IN 46500
      <b>Fairhaven</b>
      1220 Meadow Dr., Fairhaven, IN 46590
      <div class="web">Visit: www.harborviewautismcenter.example<br>E-mail: hello@harborviewautismcenter.example</div>
      <div class="call">Call: 555-014-2270</div>
    </div>
  </section>

  <!-- Outside: Page 1 (cover) -->
  <section class="panel" style="left:531px;top:50px;width:254px;height:529px">
    <div class="photo" role="img" aria-label="Photo of three smiling children hugging in a bright classroom" style="top:0;height:230px;background:linear-gradient(135deg,#a9c85a,#d9e6a0 45%,#5a7a9a 80%,#2d3e5a)"></div>
    <div class="strip" style="top:230px"><span class="b" style="width:149px"></span><span class="y" style="width:25px"></span><span class="g"></span></div>
    <div class="body pale cover" style="top:253px;height:276px">
      <div class="wordmark" style="margin-top:40px"><span class="dot"></span>Harborview</div>
      <div class="tagline" style="margin-top:52px">Hope <span>for every </span><span class="c1">child,</span><br>every <span class="c2">family.</span></div>
      <h3>ABA Therapy and Your Family</h3>
      <div class="mini">Visit: www.harborviewautismcenter.example<br>E-mail: hello@harborviewautismcenter.example<br>Call: 555-014-2270</div>
    </div>
  </section>

  <div class="page-label" style="left:24px;top:584px">Page 5</div>
  <div class="page-label" style="left:278px;top:584px">Back page 6</div>
  <div class="page-label" style="left:531px;top:584px">Page 1</div>

  <!-- Inside: Page 2 -->
  <section class="panel" style="left:24px;top:621px;width:254px;height:530px">
    <div class="photo" role="img" aria-label="Photo of a group of children and staff sitting at picnic tables outdoors" style="top:0;height:224px;background:linear-gradient(180deg,#3e6a3a,#8a7a5a 55%,#3f7fc0 100%)"></div>
    <div class="strip" style="top:224px"><span class="n" style="width:136px"></span><span class="y" style="width:38px"></span><span class="g"></span></div>
    <div class="body pale copy" style="top:249px;height:281px">
      <h2 style="margin-top:6px">How it all started.</h2>
      <p class="lead">Daniel Ashford, Executive Director, and wife, Carol Ashford, founded Harborview because they understand the frustration and feeling of helplessness when you are told your child has Autism.</p>
      <p>Our son, Owen, was diagnosed with Autism in 2003. We understand the struggles you go through as a parent when you are told that your child has Autism. That is why we created Harborview Autism Center here in Brookfield and Fairhaven, said Ashford. <b>Intensive center-based therapy made a huge difference in our son’s life – and in our lives.</b></p>
    </div>
  </section>

  <!-- Inside: Page 3 -->
  <section class="panel" style="left:278px;top:621px;width:253px;height:530px">
    <div class="body navy copy" style="top:0;height:345px;padding-top:26px">
      <h2>How can Harborview help your family?</h2>
      <p>We make every effort to help families of children with autism through the use of intensive, center based, one-on-one ABA Therapy. This approach can help teach children social, moto, communication and self-help skills. ABA works – from an 11 year old child who used the restroom for the first time to a 5 year old transitioning back to school – we see success through ABA every day.</p>
      <p>As the only center in Michiana for Autism with an award-winning management team, we know it is our child and family focused philosophy that helps us achieve enduring success. Having been in your shoes, it is our understanding that helps our parents stay strong and positive amidst daily challenges.</p>
    </div>
    <div class="strip" style="top:345px;height:26px"><span class="n" style="width:137px"></span><span class="y" style="width:37px"></span><span class="g"></span></div>
    <div class="photo" role="img" aria-label="Photo of three young children leaning on a table" style="top:371px;height:159px;background:linear-gradient(135deg,#6a8a5a,#c9a27a 45%,#8a5a3a 80%,#4a3a2a)"></div>
  </section>

  <!-- Inside: Page 4 -->
  <section class="panel" style="left:531px;top:621px;width:254px;height:530px">
    <div class="photo" role="img" aria-label="Photo of a bright playroom with a playhouse, shelves and a colorful alphabet mat" style="top:0;height:183px;background:linear-gradient(135deg,#b8d84a,#9aa8a0 40%,#d06a5a 70%,#5a8a4a)"></div>
    <div class="strip" style="top:183px"><span class="n" style="width:135px"></span><span class="y" style="width:39px"></span><span class="g"></span></div>
    <div class="body pale copy" style="top:206px;height:324px">
      <h2 style="margin-top:2px">What is ABA?</h2>
      <ul style="margin-top:12px">
        <li>ABA therapy helps to</li>
        <li>✦ Develop new skills</li>
        <li>✦ Shape and refine previously learned skills,</li>
        <li>✦ Decrease socially significant problem behaviors</li>
        <li>• It is endorsed by the US Surgeon General</li>
        <li>• Research shows it is most effected when used 25-40hours per week.</li>
      </ul>
      <h2 style="margin-top:10px">A Parents Perspective.</h2>
      <p>Before Harborview, we struggled to get Mia to connect with us. She would only communicate to address her most basic wants and needs. She would rarely even let us sit next to her,” said Mia’s mother, Jenna Hale. I am falling head over heels in love with her all over again. We have everyone at Harborview to thank for that. This is the first environment where we have seen her thrive and where she has been really happy.</p>
    </div>
  </section>

  <div class="page-label" style="left:24px;top:1160px">inside left Page 2</div>
  <div class="page-label" style="left:278px;top:1160px">inside Center Page 3</div>
  <div class="page-label" style="left:531px;top:1160px">inside Right Page 4</div>
</body>
</html>
```